Business card for my company-RKV Design Studio

I do not have a logo-I like red and keeping it clean. Information that should be on the card:
Tom Brazenhall AIA
Architecture Planning Interiors
Cell Phone-614.529.4086
email-rkvplanner4@mailvane.net
www.rkvdesignstudio.net

```html
<!DOCTYPE html>
<html lang="en">
<head>
<meta charset="utf-8">
<title>RKV Design Studio — Business Card</title>
<link rel="stylesheet" href="https://fonts.googleapis.com/css2?family=Red+Hat+Display:wght@400;500;600;700&display=swap">
<style>
  :root {
    --stage: #464648;
    --brand-red: #d3252e;
    --brand-red-light: #dc3c44;
    --card-white: #ffffff;
    --paper-tint: #f4f4f5;
    --accent-gray: #e4e4e6;
    --text-white: #ffffff;
  }
  * { margin: 0; padding: 0; box-sizing: border-box; }
  html, body {
    width: 1200px; height: 1200px; overflow: hidden;
    background: var(--stage);
    font-family: "Red Hat Display", Arial, sans-serif;
  }
  .card {
    position: absolute;
    border-radius: 31px;
    overflow: hidden;
    box-shadow: 0 4px 14px rgba(0,0,0,0.35);
  }
  .card-front { left: 233px; top: 112px; width: 736px; height: 448px; background: var(--brand-red); color: var(--text-white); }
  .card-back { left: 230px; top: 625px; width: 733px; height: 448px; background: var(--card-white); color: var(--brand-red); }

  .blueprint-backdrop { position: absolute; inset: 0; }
  .card-front .blueprint-backdrop { background: linear-gradient(160deg, #d72c35 0%, var(--brand-red) 55%, #cf222b 100%); }
  .card-back .blueprint-backdrop { background: linear-gradient(200deg, var(--paper-tint) 0%, var(--card-white) 60%); }

  .roof-drawing { position: absolute; border-radius: 4px; }
  .card-front .roof-drawing { left: 66px; top: 121px; width: 286px; height: 190px; background: linear-gradient(180deg, rgba(255,255,255,0.10), rgba(255,255,255,0.18)); }
  .card-back .roof-drawing { left: 419px; top: 223px; width: 272px; height: 103px; background: linear-gradient(180deg, rgba(211,37,46,0.06), rgba(211,37,46,0.14)); }

  .brand-name {
    position: absolute;
    display: flex; align-items: center; gap: 10px;
    font-weight: 700; font-size: 29px; line-height: 1.05; letter-spacing: 0.5px;
  }
  .brand-mark { width: 16px; height: 16px; flex: none; }
  .card-front .brand-name { left: 70px; top: 228px; width: 280px; }
  .card-front .brand-mark { background: var(--text-white); }
  .card-back .brand-name { left: 422px; top: 330px; width: 272px; color: var(--brand-red); }
  .card-back .brand-mark { background: var(--brand-red); }

  .service-list { position: absolute; left: 360px; top: 211px; list-style: none; font-weight: 500; font-size: 19px; line-height: 25px; }
  .service-list li::before { content: "·"; display: inline-block; width: 18px; font-weight: 700; }

  .tagline { position: absolute; left: 0; right: 0; top: 342px; text-align: center; font-weight: 600; font-size: 26px; word-spacing: 4px; }

  .name-marker { position: absolute; left: 3px; top: 97px; width: 53px; height: 17px; background: var(--accent-gray); }
  .person-name { position: absolute; left: 54px; top: 95px; font-weight: 400; font-size: 42px; line-height: 1; }
  .person-role { position: absolute; left: 54px; top: 143px; font-weight: 600; font-size: 25px; }

  .contact-list { position: absolute; left: 56px; top: 259px; list-style: none; font-weight: 600; font-size: 17px; line-height: 22px; }
  .contact-list li { display: flex; align-items: center; gap: 8px; }
  .contact-icon { width: 20px; height: 20px; flex: none; }
  .postal-address { position: absolute; left: 56px; top: 350px; font-style: normal; font-weight: 600; font-size: 17px; line-height: 23px; }

  .divider { position: absolute; left: 367px; top: 227px; width: 3px; height: 173px; background: var(--brand-red); }
</style>
</head>
<body>

<section class="card card-front">
  <div class="blueprint-backdrop" role="img" aria-label="Faint architectural plan drawing in the background"></div>
  <div class="roof-drawing" role="img" aria-label="Architectural section drawing of a curved-roof building"></div>
  <div class="brand-name"><span class="brand-mark"></span><span>RKV Design Studio</span></div>
  <ul class="service-list">
    <li>Residential Design</li>
    <li>Institutional &amp; Commercial Design</li>
    <li>On the Boards Design</li>
  </ul>
  <p class="tagline">Dream it.  Design it.  Build it.</p>
</section>

<section class="card card-back">
  <div class="blueprint-backdrop" role="img" aria-label="Faint architectural plan drawing in the background"></div>
  <div class="name-marker"></div>
  <h1 class="person-name">Tom Brazenhall AIA</h1>
  <p class="person-role">Architecture Planning Interiors</p>

  <ul class="contact-list">
    <li>
      <svg class="contact-icon" viewBox="0 0 24 24" aria-hidden="true"><path fill="#d3252e" d="M6.6 10.8a15 15 0 0 0 6.6 6.6l2.2-2.2c.3-.3.7-.4 1-.2 1.1.4 2.3.6 3.6.6.6 0 1 .4 1 1V20c0 .6-.4 1-1 1A17 17 0 0 1 3 4c0-.6.4-1 1-1h3.5c.6 0 1 .4 1 1 0 1.3.2 2.5.6 3.6.1.3 0 .7-.2 1z"/></svg>
      <span>614.529.4086</span>
    </li>
    <li>
      <svg class="contact-icon" viewBox="0 0 24 24" aria-hidden="true"><rect x="2" y="5" width="20" height="14" fill="#d3252e"/><path d="M2.5 5.5 12 13l9.5-7.5M2.5 18.5l7-6.5M21.5 18.5l-7-6.5" stroke="#fff" stroke-width="1.4" fill="none"/></svg>
      <span>rkvplanner4@mailvane.net</span>
    </li>
    <li>
      <svg class="contact-icon" viewBox="0 0 24 24" aria-hidden="true"><g fill="none" stroke="#d3252e" stroke-width="2"><circle cx="12" cy="12" r="9"/><ellipse cx="12" cy="12" rx="4" ry="9"/><path d="M3 12h18M4.5 7.5h15M4.5 16.5h15"/></g></svg>
      <span>www.rkvdesignstudio.net</span>
    </li>
  </ul>

  <address class="postal-address">1482 Harlow Ave. #117<br>Brookfield Heights | Ohio 43219</address>

  <div class="divider"></div>
  <div class="roof-drawing" role="img" aria-label="Architectural section drawing of a curved-roof building"></div>
  <div class="brand-name"><span class="brand-mark"></span><span>RKV Design Studio</span></div>
</section>

</body>
</html>
```